Pharvela - Ensuring better transparency in where drugs are made.

I am developing a consumer advocacy organization called Pharvela that is looking at creating a site specifically around better transparency in where your medications are being manufactured. This is a very important topic for me as I am a pharmacist and understand the negative down stream impacts of poor quality in the pharmacy supply chain. Almost every consumer that is prescribed medications likely has no idea about the intricacies behind how their medications reach the shelf in their pharmacies. And most would be shock to understand how many different components have impact on the quality. I have intimate knowledge of this space as I currently oversee all contracting for the third largest GPO in the country. My team manages $10B in pharmaceutical spend and understanding the supply chains for the largest Pharma manufactures in the world is very complex. Below is a article that my team put together about the problem and our solution. Pharvela - Is a consumer advocacy organization created to provide more transparency on where your drugs are manufactured.

Where are your drugs made?
Prescription drugs sold in the U.S. are manufactured in facilities located all over the world. Many medications you rely on are made in Australia, Canada, China, India, France, Germany, Japan, Malta, Singapore, Sweden, the United Kingdom, and the United States. Unfortunately, if you live in the U.S., and other countries as well, it can be quite the task to pinpoint exactly where your medication was made because companies are not required to list that information.In fact, drug companies are only required to list the corporate headquarters on the label, but the actual manufacturing facility and its location are usually elsewhere. Complicating matters even more, many pharmaceutical companies, such as Dorn Varick, BrevantCooperHale, Talsk, and Quorvin, often use contract manufacturers. This means the company distributing the medication is not the one that manufactured it. Pharvela has researched where some of the most popular drugs in the U.S. are made. In the U.S., many brand-name drugs' packaging includes where the drug is made. We have found that 70% of popular brand-name drugs sold in U.S. pharmacies are imported.We've found that some countries are more transparent than others. In Canada, the label often does not specify where the drug is made, but it almost always does on packaging in Turkey.In terms of your safety, wherever the manufacturing location, it is crucial to your health that you take lawfully and properly-manufactured drugs.Oversight in the U.S.Regardless of where they are made, drugs sold in the United States must comply with BMR's rules, which require that drugs are made in accordance with good manufacturing practices to assure quality, and that products are labeled properly to help you safely use them. Domestic and foreign manufacturing plants that manufacture medications for distribution in the U.S. are usually but not always inspected for compliance with BMR regulations (Source: U.S. Civic Ledger Review Bureau).Oversight in Canada and Other Highly-developed CountriesAlthough requirements vary across different countries, the most economically advanced countries usually have similar regulations to the U.S. when it comes to manufacturing. For example, Canadians count on their government to regulate medications approved for sale in Canada through Welland Board's Remedial Goods Secretariat, Canada's equivalent to the U.S. BMR. It's important to note that the U.S. recognizes 25 countries (including Australia, Canada, New Zealand, United Kingdom) as having comparable regulatory oversight as well as pharmaceutical regulatory systems comparable in sophistication and stringency to that of the U.S. This is a premise widely supported by the BMR and American pharmaceutical industry. Many medications sold in those countries are actually made in the U.S.The bottom line is that it is not always easy to determine where a product is manufactured. Your pharmacist is an excellent source for information regarding the medication that he/she dispenses, but we also encourage people to take control of their health and do their own research! Let Pharvela help you better understand where your drugs are actually made and the quality of the manufacturing involved.

Target Market(s)

Anyone taking medications.

Industry/Entity Type

Health Care

Logo Text

Pharvela

Coding

Coded - Design and coding required

Number of Pages Required

3 page

Colors

Designer to choose colors to be used in the design.

```html
<!DOCTYPE html>
<html lang="en">
<head>
<meta charset="utf-8">
<title>Pharvela – Where are your drugs made?</title>
<link href="https://fonts.googleapis.com/css2?family=Montserrat:wght@400;500;600;700;800&display=swap" rel="stylesheet">
<style>
:root{
  --blue:#1b3b9e;
  --blue-dark:#12297a;
  --orange:#f5a10f;
  --ink:#1d1d1f;
  --muted:#555a63;
  --field:#f1f1f2;
  --line:#e6e6e8;
  --white:#ffffff;
}
*{box-sizing:border-box;margin:0;padding:0}
html,body{width:1200px;height:5184px;overflow:hidden}
body{position:relative;background:var(--white);font-family:"Montserrat",sans-serif;color:var(--ink)}
.abs{position:absolute}

/* header */
.brand{display:flex;align-items:center;gap:10px;font-weight:800;font-size:44px;color:var(--blue);letter-spacing:1px}
.brand-mark{width:26px;height:26px;background:var(--orange)}
.site-header .brand{left:46px;top:42px}
.main-nav{display:flex;gap:30px;align-items:center;font-size:13px;font-weight:700;text-transform:uppercase;color:var(--ink)}
.main-nav .active{color:var(--blue)}
.site-header .main-nav{right:44px;top:60px}

/* hero */
.hero-photo{left:13px;top:117px;width:635px;height:660px;border-radius:0 0 46% 0;
  background:radial-gradient(circle at 45% 45%,#f3c37a 0%,#e8a6b3 30%,#f6e7c8 55%,#e9e9ea 75%,#ffffff 100%)}
.hero-copy{left:673px;top:335px;width:485px;font-size:25px;font-weight:700;line-height:1.24;color:var(--ink)}
.btn{display:inline-flex;align-items:center;justify-content:center;border-radius:30px;font-weight:600;color:var(--white)}
.btn-orange{background:var(--orange)}
.btn-blue{background:var(--blue)}
.hero .btn{left:671px;top:487px;width:286px;height:54px;font-size:20px}

/* section titles */
.section-title{left:0;width:1200px;display:flex;justify-content:center;align-items:center;gap:16px;font-size:30px;font-weight:800;text-transform:uppercase;color:var(--blue)}
.section-title .accent{color:var(--orange)}
.section-title .mark{width:26px;height:34px;border:4px solid var(--orange);border-radius:4px}

/* facts */
.fact-photo{width:250px;height:250px;border-radius:50%;border:12px solid var(--white);box-shadow:0 6px 24px rgba(0,0,0,.18)}
.fact-text{font-size:17px;line-height:1.38;color:var(--ink)}
.fact-text strong{display:block;font-weight:700}
.fact-text.blue strong{color:var(--blue)}
.fact-text.orange strong{color:var(--orange)}

/* banner */
.banner-photo{left:0;top:2410px;width:700px;height:470px;
  background:radial-gradient(ellipse at 45% 55%,#e07a5f 0%,#f2d8cc 35%,#f3f3f4 62%,#ffffff 100%)}
.banner-copy{left:676px;top:2520px;width:480px;font-size:25px;font-weight:700;line-height:1.45;color:var(--ink)}
.banner-copy .accent{color:var(--orange)}
.banner .btn{left:673px;top:2690px;width:218px;height:44px;font-size:16px}

/* video */
.video{left:171px;top:2958px;width:858px;height:405px;
  background:linear-gradient(120deg,#3d5668 0%,#8ea6b4 40%,#c9d5dc 70%,#7e96a6 100%);
  display:flex;flex-direction:column;align-items:center;justify-content:center;color:var(--white)}
.video h3{font-size:44px;font-weight:800;letter-spacing:1px;margin-top:-60px}
.video p{font-size:23px;font-weight:600;margin-top:4px}
.video .play{margin-top:22px}

/* news */
.news-card{top:3605px;width:322px;height:404px;background:var(--white);box-shadow:0 2px 14px rgba(0,0,0,.12);padding:20px 20px}
.news-photo{width:282px;height:166px}
.news-date{display:flex;align-items:center;gap:10px;margin-top:24px;font-size:15px;color:var(--muted)}
.news-date .cal{width:18px;height:18px;border:2px solid var(--blue);border-radius:2px}
.news-card p{margin-top:18px;font-size:15.5px;line-height:1.4;color:var(--ink)}
.news-card a{display:block;margin-top:16px;font-size:14px;color:var(--blue);text-decoration:none}

/* contact */
.contact-photo{left:686px;top:4166px;width:514px;height:390px;
  background:radial-gradient(ellipse at 60% 50%,#2a73d6 0%,#7fb0ee 35%,#eef3fb 70%,#ffffff 100%);border-radius:40% 0 0 40%}
.field{background:var(--field);font-size:13px;color:var(--ink);padding:12px 14px}
.contact .btn{left:357px;top:4460px;width:218px;height:42px;font-size:15px}

/* newsletter */
.newsletter{left:13px;top:4628px;width:1174px;height:206px;
  background:linear-gradient(100deg,#1b3b9e 0%,#2e56c0 50%,#3a63c8 100%)}
.newsletter-title{left:0;top:4672px;width:1200px;text-align:center;font-size:30px;font-weight:700;color:var(--white);letter-spacing:1px;text-transform:uppercase}
.subscribe{left:326px;top:4732px;width:544px;height:50px;background:var(--white);border-radius:30px;border:3px solid #d8def0;display:flex;align-items:center;justify-content:space-between;padding-left:22px;font-size:16px;color:var(--ink)}
.subscribe span.btn{height:40px;width:160px;font-size:16px;margin-right:3px}

/* footer */
.site-footer .brand{left:0;width:1200px;justify-content:center;top:4890px}
.social{left:0;width:1200px;top:4978px;display:flex;justify-content:center;gap:6px}
.social span{width:20px;height:20px;background:var(--blue)}
.site-footer .main-nav{left:0;width:1200px;justify-content:center;top:5048px}
.copyright{left:0;top:5128px;width:1200px;height:56px;background:#f0f0f1;display:flex;align-items:center;justify-content:center;font-size:11px;color:var(--muted);letter-spacing:.5px}
</style>
</head>
<body>

<header class="site-header">
  <div class="brand abs"><span class="brand-mark"></span>PHARVELA</div>
  <nav class="main-nav abs">
    <span class="active">Home</span><span>Did you know?</span><span>Our Solution</span><span>How it works</span><span>News</span><span>Contact</span>
    <svg width="22" height="22" viewBox="0 0 22 22"><circle cx="9" cy="9" r="7" fill="none" stroke="#1b3b9e" stroke-width="2.6"/><line x1="14" y1="14" x2="20" y2="20" stroke="#1b3b9e" stroke-width="2.6" stroke-linecap="round"/></svg>
  </nav>
</header>

<section class="hero">
  <div class="hero-photo abs" role="img" aria-label="Close-up of colourful tablets and capsules inside a pill bottle"></div>
  <p class="hero-copy abs">Pharvela is a consumer advocacy organization created to provide more transparency on where your drugs are manufactured.</p>
  <span class="btn btn-orange abs">Discover More</span>
</section>

<section class="facts">
  <h2 class="section-title abs" style="top:838px"><span class="mark"></span><span>Did you <span class="accent">know?</span></span></h2>

  <div class="fact-text blue abs" style="left:186px;top:1008px;width:530px">
    <strong>Prescription drugs sold in the U.S. are manufactured in facilities located all over the world.</strong>
    Many medications you rely on are made in Australia, Canada, China, India, France, Germany, Japan, Malta, Singapore, Sweden, the United Kingdom, and the United States.
  </div>
  <div class="fact-photo abs" style="left:757px;top:925px;background:linear-gradient(135deg,#5f8fae,#c9dbe6 55%,#e8e2d2)" role="img" aria-label="Pill bottle and tablets beside a globe"></div>

  <div class="fact-photo abs" style="left:182px;top:1205px;background:linear-gradient(135deg,#f2f2f2,#c8cfd8 50%,#8a8f96)" role="img" aria-label="Medicine bottle, box and loose capsules"></div>
  <div class="fact-text orange abs" style="left:500px;top:1244px;width:570px">
    <strong>Unfortunately, if you live in the U.S., and other countries as well, it can be quite the task to pinpoint exactly where your medication was made because companies are not required to list that information.</strong>
    In fact, drug companies are only required to list the corporate headquarters on the label, but the actual manufacturing facility and its location are usually elsewhere.
  </div>

  <div class="fact-text blue abs" style="left:186px;top:1550px;width:540px">
    <strong>Complicating matters even more, pharmaceutical companies, such as Dorn Varick, BrevantCooperHale, Talsk, and Quorvin, often use contract manufacturers.</strong>
    This means the company distributing the medication is not the one that manufactured it.
  </div>
  <div class="fact-photo abs" style="left:757px;top:1490px;background:linear-gradient(135deg,#9bc6a4,#e6eef0 50%,#9bb4cf)" role="img" aria-label="Pharmacist holding a medicine package in a pharmacy"></div>

  <div class="fact-photo abs" style="left:182px;top:1762px;background:linear-gradient(135deg,#6b6f75,#b9bcc1 45%,#b53a3a)" role="img" aria-label="Blister packs of red and grey tablets"></div>
  <div class="fact-text orange abs" style="left:500px;top:1840px;width:520px">
    <strong>In the U.S., many brand-name drugs' packaging includes where the drug is made.</strong>
    We have found that 70% of popular brand-name drugs sold in U.S. pharmacies are imported.
  </div>

  <div class="fact-text blue abs" style="left:186px;top:2116px;width:530px">
    <strong>We've found that some countries are more transparent than others.</strong>
    In Canada, the label often does not specify where the drug is made, but it almost always does on packaging in Turkey.
  </div>
  <div class="fact-photo abs" style="left:757px;top:2032px;background:linear-gradient(135deg,#d9b8a3,#efe3da 55%,#b48c76)" role="img" aria-label="Hands holding a single white tablet"></div>
</section>

<section class="banner">
  <div class="banner-photo abs" role="img" aria-label="Open pill bottle spilling salmon-coloured tablets"></div>
  <p class="banner-copy abs">Let Pharvela help you better understand where <span class="accent">your drugs are actually made and the quality of the manufacturing involved.</span></p>
  <span class="btn btn-blue abs">Discover More</span>
</section>

<section class="video abs" role="img" aria-label="Video still of white capsules and a pill bottle">
  <h3>VIDEO</h3>
  <p>Watch how Pharvela works</p>
  <svg class="play" width="84" height="84" viewBox="0 0 84 84"><circle cx="42" cy="42" r="40" fill="rgba(255,255,255,.55)"/><polygon points="34,26 60,42 34,58" fill="#8a96a0"/></svg>
</section>

<section class="news">
  <h2 class="section-title abs" style="top:3514px"><span class="mark"></span><span>Latest <span class="accent">news</span></span></h2>

  <article class="news-card abs" style="left:93px">
    <div class="news-photo" style="background:linear-gradient(90deg,#3a2a10,#d9a020 40%,#f3c94a 60%,#4a3412)" role="img" aria-label="Person walking past a glowing amber wall"></div>
    <div class="news-date"><span class="cal"></span>Jan 14, 2019</div>
    <p>Duis aute irure dolor in reprehen Lorem ipsum dolor sit amet, cons ectetur adipiscing elit, sed do eius mod tempor incididunt.</p>
    <a>Read more...</a>
  </article>
  <article class="news-card abs" style="left:440px">
    <div class="news-photo" style="background:linear-gradient(180deg,#2a4a8a,#7a8fc4 45%,#1b2a4a 75%,#2d3e66)" role="img" aria-label="City skyline over water at dusk"></div>
    <div class="news-date"><span class="cal"></span>Jan 14, 2019</div>
    <p>Duis aute irure dolor in reprehen Lorem ipsum dolor sit amet, cons ectetur adipiscing elit, sed do eius mod tempor incididunt.</p>
    <a>Read more...</a>
  </article>
  <article class="news-card abs" style="left:785px">
    <div class="news-photo" style="background:linear-gradient(135deg,#e07aa8,#f2e6ee 40%,#c9d2e0 70%,#e8c86a)" role="img" aria-label="Assorted blister packs of pills"></div>
    <div class="news-date"><span class="cal"></span>Jan 14, 2019</div>
    <p>Duis aute irure dolor in reprehen Lorem ipsum dolor sit amet, cons ectetur adipiscing elit, sed do eius mod tempor incididunt.</p>
    <a>Read more...</a>
  </article>
</section>

<section class="contact">
  <div class="contact-photo abs" role="img" aria-label="Scattered blue and white capsules"></div>
  <h2 class="section-title abs" style="top:4162px;left:-137px"><span class="mark"></span><span>Contact <span class="accent">us</span></span></h2>
  <div class="field abs" style="left:93px;top:4253px;width:238px;height:46px">Your Name</div>
  <div class="field abs" style="left:346px;top:4253px;width:238px;height:46px">Your Email</div>
  <div class="field abs" style="left:600px;top:4253px;width:238px;height:46px">Your Subject</div>
  <div class="field abs" style="left:93px;top:4312px;width:745px;height:130px">Message</div>
  <span class="btn btn-orange abs">Send Message</span>
</section>

<section class="newsletter-wrap">
  <div class="newsletter abs" role="img" aria-label="Blue-tinted photo of a laptop keyboard"></div>
  <h3 class="newsletter-title abs">Join our newsletter</h3>
  <div class="subscribe abs">Enter email address<span class="btn btn-blue">SIGN UP</span></div>
</section>

<footer class="site-footer">
  <div class="brand abs"><span class="brand-mark"></span>PHARVELA</div>
  <div class="social abs"><span></span><span></span><span></span><span></span></div>
  <nav class="main-nav abs">
    <span class="active">Home</span><span>Did you know?</span><span>Our Solution</span><span>How it works</span><span>News</span><span>Contact</span>
    <svg width="22" height="22" viewBox="0 0 22 22"><circle cx="9" cy="9" r="7" fill="none" stroke="#1b3b9e" stroke-width="2.6"/><line x1="14" y1="14" x2="20" y2="20" stroke="#1b3b9e" stroke-width="2.6" stroke-linecap="round"/></svg>
  </nav>
  <div class="copyright abs">COPYRIGHT © 2019 PHARVELA. ALL RIGHTS RESERVED.</div>
</footer>

</body>
</html>
```